Quorvel Business Card

Looking for business card ideas. Company name is Quorvel. Have a few basic ideas on attachment. Please submit anything with the logo and general information from attachment.

Industry/Entity Type

Business

```html
<!DOCTYPE html>
<html lang="en">
<head>
<meta charset="utf-8">
<title>Quorvel Business Card</title>
<link rel="stylesheet" href="https://fonts.googleapis.com/css2?family=Open+Sans:wght@400;600;700&display=swap">
<style>
  :root {
    --stage: #3b3b3d;
    --card: #262628;
    --logo-panel: #58595b;
    --name-grey: #6d6e70;
    --text-light: #f2f2f2;
    --pill: #a8c7ce;
    --pill-text: #6f8990;
  }
  * { margin: 0; padding: 0; box-sizing: border-box; }
  html, body {
    width: 1200px;
    height: 800px;
    overflow: hidden;
    background: var(--stage);
    font-family: "Open Sans", Arial, sans-serif;
  }
  .stage {
    width: 1200px;
    height: 800px;
    display: flex;
    align-items: center;
    justify-content: center;
  }
  .business-card {
    position: relative;
    width: 900px;
    height: 514px;
    background: var(--card);
    border-radius: 4px;
    overflow: hidden;
  }
  .holder {
    position: absolute;
    left: 70px;
    top: 58px;
  }
  .holder-name {
    font-size: 30px;
    font-weight: 700;
    color: var(--name-grey);
    line-height: 1.1;
  }
  .holder-role {
    font-size: 22px;
    font-weight: 400;
    color: var(--text-light);
    line-height: 1.3;
  }
  .logo-panel {
    position: absolute;
    left: 130px;
    top: 140px;
    width: 330px;
    height: 240px;
    background: var(--logo-panel);
    border-radius: 34px;
    display: flex;
    align-items: center;
    justify-content: center;
  }
  .brand-name {
    font-size: 40px;
    font-weight: 600;
    color: var(--text-light);
  }
  .contact-list {
    position: absolute;
    left: 530px;
    top: 60px;
    list-style: none;
    font-size: 20px;
    font-weight: 400;
    color: var(--text-light);
    line-height: 1.6;
  }
  .contact-list .label { margin-left: 14px; }
  .address-pill {
    position: absolute;
    left: 380px;
    right: 40px;
    top: 400px;
    height: 66px;
    background: var(--pill);
    border-radius: 33px;
    display: flex;
    align-items: center;
    justify-content: space-between;
    padding: 0 40px;
    font-size: 20px;
    font-style: normal;
    color: var(--pill-text);
  }
</style>
</head>
<body>
  <main class="stage">
    <article class="business-card">
      <header class="holder">
        <p class="holder-name">Dana Verlo</p>
        <p class="holder-role">Director</p>
      </header>

      <div class="logo-panel">
        <span class="brand-name">Quorvel</span>
      </div>

      <ul class="contact-list">
        <li>www.quorvel.org</li>
        <li>dverlo@quorvelmail.com</li>
        <li>(555) 014-2290<span class="label">Cell</span></li>
        <li>(555) 014-7365<span class="label">Office</span></li>
      </ul>

      <address class="address-pill">
        <span class="address-city">Fenwick, TX 70142</span>
        <span class="address-street">2480 N. Alder Row</span>
      </address>
    </article>
  </main>
</body>
</html>
```